Flyer-Design für psychologische Beratungspraxis für Mütter
Zielgruppe
Gelassenheitswerkstatt ist eine psychologische Beratungspraxis. Ich unterstütze Mütter, Schwangere und Frauen mit Kinderwunsch bei Herausforderungen rund um Schwangerschaft, Geburt, Mutterschaft, und damit einhergehenden Problemen.
Aufgabenstellung
Text nochmal geringgradig geändert...siehe Datei anbei

```html
<!DOCTYPE html>
<html lang="de">
<head>
<meta charset="utf-8">
<title>Gelassenheitswerkstatt – Flyer</title>
<link rel="stylesheet" href="https://fonts.googleapis.com/css2?family=Montserrat:wght@500;600;700;800&family=Raleway:wght@300;400;700&family=Kalam:wght@400&display=swap">
<style>
:root{
  --navy:#1b3a73;
  --navy-deep:#0f3c78;
  --brand-navy:#2b2c7c;
  --green:#6aab2e;
  --orange:#e9542a;
  --ink:#222;
  --paper:#fff;
  --bg:#fff;
  --sketch:#fbfbfb;
}
*{margin:0;padding:0;box-sizing:border-box}
html,body{width:693px;height:1200px;overflow:hidden;background:var(--bg)}
.sheet{position:relative;width:693px;height:1200px;overflow:hidden;font-family:"Raleway",sans-serif;color:var(--ink)}

/* brand header */
.brand-rule{position:absolute;height:1.2px;background:var(--green)}
.brand-rule--left{left:0;top:123px;width:261px;transform:rotate(0.4deg)}
.brand-rule--right{left:424px;top:106px;width:269px;transform:rotate(-1.5deg)}
.brand{position:absolute;left:243px;top:40px;width:200px;text-align:center}
.brand__dot{display:block;width:54px;height:54px;border-radius:50%;background:var(--orange);margin:0 auto 24px}
.brand__name{font-family:"Montserrat",sans-serif;font-weight:600;font-size:13px;color:var(--brand-navy)}

.version-label{position:absolute;left:41px;font-family:"Montserrat",sans-serif;font-weight:700;font-size:7px;color:#222}

/* panels */
.panel{position:absolute;left:25px;width:643px;height:219px;background:var(--paper);box-shadow:0 1px 6px rgba(0,0,0,.12);overflow:hidden}
.abs{position:absolute;white-space:nowrap}

.mark{position:absolute;text-align:center}
.mark__dot{display:block;border-radius:50%;background:var(--orange);margin:0 auto}
.mark__name{font-family:"Montserrat",sans-serif;font-weight:600;color:var(--brand-navy)}

/* cover — inner side */
.cover__figure{position:absolute;left:0;top:53px;width:100px;height:141px;background:linear-gradient(180deg,#fcfcfc,var(--sketch))}
.cover__headline{font-family:"Montserrat",sans-serif;font-weight:800;font-size:10px;color:var(--navy);letter-spacing:.1px}
.cover__body{font-size:5.6px;font-weight:300;color:#222}
.cover__body--strong{font-weight:700}
.cover__curve{position:absolute;left:0;top:0}
.cover__script{font-family:"Kalam",cursive;font-size:9.5px;color:var(--green);transform:rotate(-6deg);transform-origin:left center}
.cover__portrait{position:absolute;left:327px;top:10px;width:69px;height:69px;border-radius:50%;background:linear-gradient(180deg,#6f9fd6 0%,#9dc0e3 55%,#b99a70 78%,#4a4030 100%)}
.cover__service{left:213px;width:213px;text-align:center;font-family:"Montserrat",sans-serif;font-size:5.2px;font-weight:500;color:var(--navy)}
.cover__person{left:213px;width:213px;text-align:center;font-family:"Montserrat",sans-serif;font-size:4px;color:var(--navy)}
.cover__person--strong{font-weight:700}
.cover__contact{font-family:"Montserrat",sans-serif;font-size:4px;color:var(--navy)}
.cover__contact em{font-style:normal;color:var(--green)}
.flags{position:absolute;left:351px;top:188px;display:flex;gap:3px}
.flag{width:8px;height:5px;display:block}
.flag--de{background:linear-gradient(180deg,#000 33%,#dd0000 33% 66%,#ffce00 66%)}
.flag--it{background:linear-gradient(90deg,#009246 33%,#fff 33% 66%,#ce2b37 66%)}
.flag--uk{background:linear-gradient(90deg,transparent 42%,#c8102e 42% 58%,transparent 58%),linear-gradient(180deg,#012169 38%,#c8102e 38% 62%,#012169 62%)}
.flag--fr{background:linear-gradient(90deg,#0055a4 33%,#fff 33% 66%,#ef4135 66%)}

/* cover — front */
.cover__front{position:absolute;left:426px;top:0;width:217px;height:219px}
.cover__photo{position:absolute;left:0;top:0;width:217px}
.cover--v01 .cover__photo{height:150px;background:linear-gradient(180deg,rgba(255,255,255,0) 65%,#fff 100%),linear-gradient(90deg,#f1f1f1 0%,#ebebeb 50%,#e2dcd2 75%,#e9e9e9 100%)}
.cover--v02 .cover__photo{height:160px;background:linear-gradient(180deg,rgba(255,255,255,0) 75%,#fff 100%),linear-gradient(100deg,#d9b98a 0%,#c29a66 35%,#8a6a4c 62%,#7a5e45 82%,#6a5646 100%)}
.cover__badge{position:absolute;left:20px;top:0;width:63px;height:67px;background:#fff;border-radius:0 0 8px 8px}
.cover__drawing{position:absolute;left:87px;top:30px;width:91px;height:114px;background:var(--sketch)}
.cover__title{left:0;width:217px;text-align:center;font-family:"Montserrat",sans-serif;font-weight:800;font-size:10.3px;color:var(--navy)}
.cover__subtitle{left:0;width:217px;text-align:center;font-family:"Montserrat",sans-serif;font-weight:700;font-size:5.5px;color:var(--green)}

/* inside spread */
.spread__col{position:absolute;top:0;height:219px}
.spread__col--left{left:0;width:217px}
.spread__col--mid{left:217px;width:213px;background:var(--navy-deep)}
.spread__col--right{left:430px;width:213px}
.spread__headline{font-family:"Montserrat",sans-serif;font-weight:800;font-size:10.5px;color:var(--navy)}
.spread__headline--light{color:#fff}
.spread__text{font-size:5.6px;font-weight:300;color:#222}
.spread__text b{font-weight:700}
.spread__list{font-size:5.4px;font-weight:300;color:#fff}
.spread__list b{font-weight:700}
.spread__list i{font-style:italic}
.spread__figure{position:absolute;background:var(--sketch)}
.spread__figure--dark{background:#11407d}
.spread__para{position:absolute;font-size:5.6px;font-weight:300;line-height:8.6px;color:#222;white-space:normal}
.spread__para b{font-weight:700}
.spread__signature{right:9px;text-align:right;font-size:3.4px;line-height:4.6px;color:#444}
</style>
</head>
<body>
<div class="sheet">

  <div class="brand-rule brand-rule--left"></div>
  <div class="brand-rule brand-rule--right"></div>
  <div class="brand">
    <span class="brand__dot"></span>
    <span class="brand__name">Gelassenheitswerkstatt</span>
  </div>

  <!-- Version 01 -->
  <div class="version-label" style="top:196px">V01</div>
  <section class="panel cover cover--v01" style="top:211px">
    <div class="cover__figure" role="img" aria-label="Linienzeichnung einer sitzenden Schwangeren"></div>
    <svg class="cover__curve" width="643" height="219" viewBox="0 0 643 219"><path d="M0,194 L105,194 C170,198 228,198 242,160 C252,130 244,100 244,78 C244,62 236,55 241,51" fill="none" stroke="#6aab2e" stroke-width="0.8"/></svg>
    <div class="abs cover__headline" style="left:66px;top:42px">MUTTER SEIN</div>
    <div class="abs cover__headline" style="left:76px;top:55px">IST WUNDERBAR.</div>
    <div class="abs cover__body" style="left:79.5px;top:79px">Wenn eine Frau Mutter wird, ist sie</div>
    <div class="abs cover__body" style="left:81px;top:87.6px">plötzlich verliebt über beide</div>
    <div class="abs cover__body" style="left:86px;top:96.2px">Ohren, unbändig stolz und von</div>
    <div class="abs cover__body" style="left:90.4px;top:104.8px">Glücksgefühlen völlig über-</div>
    <div class="abs cover__body" style="left:92.8px;top:113.3px">wältigt.</div>
    <div class="abs cover__body cover__body--strong" style="left:95.6px;top:121.2px">So ist es doch „NORMAL“,</div>
    <div class="abs cover__body cover__body--strong" style="left:95.6px;top:129.7px">oder…?</div>
    <div class="abs cover__script" style="left:240px;top:38px">Ich berate und</div>
    <div class="abs cover__script" style="left:252px;top:49px">begleite Sie gerne.</div>
    <div class="cover__portrait" role="img" aria-label="Porträtfoto der Beraterin an einem Wegweiser vor blauem Himmel"></div>
    <div class="mark" style="left:270px;top:100px;width:100px"><span class="mark__dot" style="width:16px;height:16px;margin-bottom:8px"></span><span class="mark__name" style="font-size:5.5px">Gelassenheitswerkstatt</span></div>
    <div class="abs cover__service" style="top:145px">SYSTEMISCHE BERATUNG &amp; COACHING</div>
    <div class="abs cover__person" style="top:160px">DR. HELENA VARWICK</div>
    <div class="abs cover__person cover__person--strong" style="top:165.5px">SYSTEMISCHE BERATERIN (VSBe) – HEILPRAKTIKERIN FÜR PSYCHOTHERAPIE</div>
    <div class="abs cover__contact" style="left:242px;top:180.5px">WWW.GELASSENHEITS<em>WERKSTATT</em>.DE</div>
    <div class="abs cover__contact" style="left:242px;top:188.5px">INFO@GELASSENHEITS<em>WERKSTATT</em>.DE</div>
    <div class="abs cover__contact" style="left:343px;top:180.5px">TELEFON: 0151 482 17 305</div>
    <div class="flags"><span class="flag flag--de"></span><span class="flag flag--it"></span><span class="flag flag--uk"></span><span class="flag flag--fr"></span></div>
    <div class="cover__front">
      <div class="cover__photo" role="img" aria-label="Foto einer lachenden Mutter mit Tochter, auf dem Boden sitzend"></div>
      <div class="mark" style="left:10px;top:16px;width:80px"><span class="mark__dot" style="width:26px;height:26px;margin-bottom:14px"></span><span class="mark__name" style="font-size:6px">Gelassenheitswerkstatt</span></div>
      <div class="abs cover__title" style="top:146px">KRISENBEGLEITUNG</div>
      <div class="abs cover__title" style="top:159px">UND LEBENSBERATUNG</div>
      <div class="abs cover__subtitle" style="top:176px">Psychologische Beratungspraxis für</div>
      <div class="abs cover__subtitle" style="top:183px">Mütter, Schwangere und Frauen mit Kinderwunsch</div>
    </div>
  </section>

  <!-- Version 02 -->
  <div class="version-label" style="top:442px">V02</div>
  <section class="panel cover cover--v02" style="top:455px">
    <div class="cover__figure" role="img" aria-label="Linienzeichnung einer sitzenden Schwangeren"></div>
    <svg class="cover__curve" width="643" height="219" viewBox="0 0 643 219"><path d="M0,194 L105,194 C170,198 228,198 242,160 C252,130 244,100 244,78 C244,62 236,55 241,51" fill="none" stroke="#6aab2e" stroke-width="0.8"/></svg>
    <div class="abs cover__headline" style="left:66px;top:42px">MUTTER SEIN</div>
    <div class="abs cover__headline" style="left:76px;top:55px">IST WUNDERBAR.</div>
    <div class="abs cover__body" style="left:79.5px;top:79px">Wenn eine Frau Mutter wird, ist sie</div>
    <div class="abs cover__body" style="left:81px;top:87.6px">plötzlich verliebt über beide</div>
    <div class="abs cover__body" style="left:86px;top:96.2px">Ohren, unbändig stolz und von</div>
    <div class="abs cover__body" style="left:90.4px;top:104.8px">Glücksgefühlen völlig über-</div>
    <div class="abs cover__body" style="left:92.8px;top:113.3px">wältigt.</div>
    <div class="abs cover__body cover__body--strong" style="left:95.6px;top:121.2px">So ist es doch „NORMAL“,</div>
    <div class="abs cover__body cover__body--strong" style="left:95.6px;top:129.7px">oder…?</div>
    <div class="abs cover__script" style="left:240px;top:38px">Ich berate und</div>
    <div class="abs cover__script" style="left:252px;top:49px">begleite Sie gerne.</div>
    <div class="cover__portrait" role="img" aria-label="Porträtfoto der Beraterin an einem Wegweiser vor blauem Himmel"></div>
    <div class="mark" style="left:270px;top:100px;width:100px"><span class="mark__dot" style="width:16px;height:16px;margin-bottom:8px"></span><span class="mark__name" style="font-size:5.5px">Gelassenheitswerkstatt</span></div>
    <div class="abs cover__service" style="top:145px">PSYCHOLOGISCHE BERATUNGSPRAXIS</div>
    <div class="abs cover__person" style="top:160px">DR. HELENA VARWICK</div>
    <div class="abs cover__person cover__person--strong" style="top:165.5px">SYSTEMISCHE BERATERIN (VSBe) – HEILPRAKTIKERIN FÜR PSYCHOTHERAPIE</div>
    <div class="abs cover__contact" style="left:242px;top:180.5px">WWW.GELASSENHEITS<em>WERKSTATT</em>.DE</div>
    <div class="abs cover__contact" style="left:242px;top:188.5px">INFO@GELASSENHEITS<em>WERKSTATT</em>.DE</div>
    <div class="abs cover__contact" style="left:343px;top:180.5px">TELEFON: 0151 482 17 305</div>
    <div class="flags"><span class="flag flag--de"></span><span class="flag flag--it"></span><span class="flag flag--uk"></span><span class="flag flag--fr"></span></div>
    <div class="cover__front">
      <div class="cover__photo" role="img" aria-label="Foto von Mutter und Tochter Hand in Hand am See im Abendlicht"></div>
      <div class="cover__badge"></div>
      <div class="mark" style="left:20px;top:12px;width:63px"><span class="mark__dot" style="width:18px;height:18px;margin-bottom:12px"></span><span class="mark__name" style="font-size:4.6px">Gelassenheitswerkstatt</span></div>
      <div class="abs cover__title" style="top:146px">KRISENBEGLEITUNG</div>
      <div class="abs cover__title" style="top:159px">UND LEBENSBERATUNG</div>
      <div class="abs cover__subtitle" style="top:176px">Psychologische Beratungspraxis für</div>
      <div class="abs cover__subtitle" style="top:183px">Mütter, Schwangere und Frauen mit Kinderwunsch</div>
    </div>
  </section>

  <!-- Version 03 -->
  <div class="version-label" style="top:686px">V03</div>
  <section class="panel cover cover--v03" style="top:698px">
    <div class="cover__figure" role="img" aria-label="Linienzeichnung einer sitzenden Schwangeren"></div>
    <div class="cover__front">
      <div class="cover__drawing" role="img" aria-label="Linienzeichnung von Mutter und Kind, von hinten gesehen"></div>
    </div>
    <svg class="cover__curve" width="643" height="219" viewBox="0 0 643 219"><path d="M0,194 L105,194 C170,198 228,198 242,160 C252,130 244,100 244,78 C244,62 236,55 241,51" fill="none" stroke="#6aab2e" stroke-width="0.8"/><path d="M401,51 C416,49 416,78 424,104 C434,132 466,136 515,137 C560,138 600,141 643,142" fill="none" stroke="#6aab2e" stroke-width="0.8"/></svg>
    <div class="abs cover__headline" style="left:66px;top:42px">MUTTER SEIN</div>
    <div class="abs cover__headline" style="left:76px;top:55px">IST WUNDERBAR.</div>
    <div class="abs cover__body" style="left:79.5px;top:79px">Wenn eine Frau Mutter wird, ist sie</div>
    <div class="abs cover__body" style="left:81px;top:87.6px">plötzlich verliebt über beide</div>
    <div class="abs cover__body" style="left:86px;top:96.2px">Ohren, unbändig stolz und von</div>
    <div class="abs cover__body" style="left:90.4px;top:104.8px">Glücksgefühlen völlig über-</div>
    <div class="abs cover__body" style="left:92.8px;top:113.3px">wältigt.</div>
    <div class="abs cover__body cover__body--strong" style="left:95.6px;top:121.2px">So ist es doch „NORMAL“,</div>
    <div class="abs cover__body cover__body--strong" style="left:95.6px;top:129.7px">oder…?</div>
    <div class="abs cover__script" style="left:240px;top:38px">Ich berate und</div>
    <div class="abs cover__script" style="left:252px;top:49px">begleite Sie gerne.</div>
    <div class="cover__portrait" role="img" aria-label="Porträtfoto der Beraterin an einem Wegweiser vor blauem Himmel"></div>
    <div class="mark" style="left:270px;top:100px;width:100px"><span class="mark__dot" style="width:16px;height:16px;margin-bottom:8px"></span><span class="mark__name" style="font-size:5.5px">Gelassenheitswerkstatt</span></div>
    <div class="abs cover__service" style="top:145px">SYSTEMISCHE BERATUNG &amp; COACHING</div>
    <div class="abs cover__person" style="top:160px">DR. HELENA VARWICK</div>
    <div class="abs cover__person cover__person--strong" style="top:165.5px">SYSTEMISCHE BERATERIN (VSBe) – HEILPRAKTIKERIN FÜR PSYCHOTHERAPIE</div>
    <div class="abs cover__contact" style="left:242px;top:180.5px">WWW.GELASSENHEITS<em>WERKSTATT</em>.DE</div>
    <div class="abs cover__contact" style="left:242px;top:188.5px">INFO@GELASSENHEITS<em>WERKSTATT</em>.DE</div>
    <div class="abs cover__contact" style="left:343px;top:180.5px">TELEFON: 0151 482 17 305</div>
    <div class="flags"><span class="flag flag--de"></span><span class="flag flag--it"></span><span class="flag flag--uk"></span><span class="flag flag--fr"></span></div>
    <div class="cover__front">
      <div class="mark" style="left:16px;top:11px;width:60px"><span class="mark__dot" style="width:18px;height:18px;margin-bottom:12px"></span><span class="mark__name" style="font-size:4.6px">Gelassenheitswerkstatt</span></div>
      <div class="abs cover__title" style="top:146px">KRISENBEGLEITUNG</div>
      <div class="abs cover__title" style="top:159px">UND LEBENSBERATUNG</div>
      <div class="abs cover__subtitle" style="top:176px">Psychologische Beratungspraxis für</div>
      <div class="abs cover__subtitle" style="top:183px">Mütter, Schwangere und Frauen mit Kinderwunsch</div>
    </div>
  </section>

  <!-- Inside spread -->
  <section class="panel spread" style="top:942px">
    <div class="spread__col spread__col--left">
      <div class="spread__figure" style="left:18px;top:29px;width:82px;height:171px" role="img" aria-label="Linienzeichnung einer Mutter mit Baby im Tragetuch"></div>
      <div class="mark" style="left:10px;top:13px;width:40px"><span class="mark__dot" style="width:12px;height:12px;margin-bottom:6px"></span><span class="mark__name" style="font-size:3.6px">Gelassenheitswerkstatt</span></div>
      <div class="abs spread__headline" style="left:85.7px;top:16px">ÜBERFORDERUNG,</div>
      <div class="abs spread__headline" style="left:85.7px;top:29px">FRUSTRATION UND</div>
      <div class="abs spread__headline" style="left:85.7px;top:42px">VERZWEIFLUNG</div>
      <div class="abs spread__text" style="left:85px;top:57.5px">kennen Mütter, Frauen mit Kinderwunsch und</div>
      <div class="abs spread__text" style="left:85px;top:66px">werdende Mütter allerdings ebenfalls nur zu</div>
      <div class="abs spread__text" style="left:94.7px;top:74.6px">gut. Wichtig ist, dass die Beurteilung einer</div>
      <div class="abs spread__text" style="left:104.7px;top:83.2px">Situation, d.h. wie stark sie uns belastet</div>
      <div class="abs spread__text" style="left:107px;top:91.7px">alleine uns selbst zusteht. Nur unsere</div>
      <div class="abs spread__text" style="left:107px;top:100.3px">eigene <b>subjektive Einschätzung</b> ist</div>
      <div class="abs spread__text" style="left:107px;top:108.8px">ausschlaggebend.</div>
      <div class="abs spread__text" style="left:109.5px;top:121.2px">So unterschiedlich wir Menschen</div>
      <div class="abs spread__text" style="left:109.5px;top:129.8px">sind, so verschieden ist nämlich</div>
      <div class="abs spread__text" style="left:109.5px;top:138.3px">auch unser persönliches Fühlen und</div>
      <div class="abs spread__text" style="left:109.5px;top:146.9px">Erleben. Deshalb benötigen wir</div>
      <div class="abs spread__text" style="left:107.6px;top:155.5px"><b>individuell passende Lösungen</b> für</div>
      <div class="abs spread__text" style="left:108px;top:164px">unsere Herausforderungen.</div>
    </div>

    <div class="spread__col spread__col--mid">
      <div class="spread__figure spread__figure--dark" style="left:6px;top:96px;width:45px;height:109px" role="img" aria-label="Linienzeichnung einer Mutter mit Baby auf dem Arm"></div>
      <div class="abs spread__headline spread__headline--light" style="left:16px;top:16px">WAS ALSO WENN…</div>
      <div class="abs spread__list" style="left:16px;top:31.7px">… wir gern <b>Mutter</b> wären, aber das Leben andere Pläne hat?</div>
      <div class="abs spread__list" style="left:16px;top:43.6px">… uns die Erfahrung der <b>Geburt belastet</b>, aber niemand zuhört,</div>
      <div class="abs spread__list" style="left:21.5px;top:52.2px">weil ja <i>„jetzt alles ok sei“</i>?</div>
      <div class="abs spread__list" style="left:16px;top:64.1px">… wenn wir unser <b>Kind</b> verloren haben?</div>
      <div class="abs spread__list" style="left:16px;top:76px">… unser Kind oder wir selbst mit einer <b>Krankheit</b> zu kämpfen haben?</div>
      <div class="abs spread__list" style="left:41px;top:87.9px">… wir selbst oder unser Partner uns <b>kaum</b></div>
      <div class="abs spread__list" style="left:45.8px;top:96.5px"><b>wiedererkennen</b>?</div>
      <div class="abs spread__list" style="left:53px;top:108.4px">… wenn wir uns treu bleiben wollen aber uns dennoch</div>
      <div class="abs spread__list" style="left:53px;top:117px">durch die Meinung anderer <b>verunsichern</b> lassen?</div>
      <div class="abs spread__list" style="left:59px;top:128.9px">… wir eben <b>nicht stolz</b> darauf sind wie wir den</div>
      <div class="abs spread__list" style="left:59px;top:137.4px">letzten Schreianfall unseres Baby begleitet haben?</div>
      <div class="abs spread__list" style="left:63.4px;top:149.3px">… wir weder die <b>Wut</b> unseres Kindes, noch unsere</div>
      <div class="abs spread__list" style="left:63.4px;top:157.9px">eigene Wut gebändigt bekommen?</div>
      <div class="abs spread__list" style="left:63.4px;top:169.8px">… wir mit der Situation <b>überfordert</b> sind und nicht</div>
      <div class="abs spread__list" style="left:67.6px;top:178.4px">mehr weiter wissen?</div>
    </div>

    <div class="spread__col spread__col--right">
      <div class="spread__figure" style="left:136px;top:10px;width:68px;height:96px" role="img" aria-label="Linienzeichnung einer sitzenden Mutter, die ihr Kind hochhebt"></div>
      <div class="abs spread__headline" style="left:14px;top:16px">JA, MUTTER SEIN IST</div>
      <div class="abs spread__headline" style="left:14px;top:29px">WUNDERVOLL!</div>
      <p class="spread__para" style="left:14px;top:44px;width:122px">Und ja, die Dynamik der Paarbeziehung verändert sich schlagartig und wir stehen plötzlich vor einer der erfüllendsten Aufgaben und zugleich einer der größten <b>existentiellen Herausforderungen</b> die uns das Leben bietet.</p>
      <div class="abs spread__headline" style="left:27px;top:112px">ELTERN SEIN.</div>
      <p class="spread__para" style="left:27px;top:126px;width:164px">Um trotz Rückschlägen ein zufriedenes Leben zu führen und um feinfühlig für unsere Kinder da zu sein, benötigen wir viel Kraft. Mentale Kraft, die es uns ermöglicht aus den Augen unserer Kinder zu sehen, unsere eigenen Gefühle zu regulieren und die starken Gefühle unserer Kinder auszuhalten und zu begleiten.</p>
      <p class="spread__para" style="left:27px;top:180px;width:164px">Gemeinsam erarbeiten wir <b>individuelle Strategien</b>, wie Sie auf Ihre eigenen Ressourcen besser zugreifen, und so mental gestärkt nach vorne schauen können.</p>
      <div class="abs spread__signature" style="top:205px">Dr. Helena Varwick<br>Systemische Beraterin (VSBe) – Heilpraktikerin für Psychotherapie</div>
    </div>

    <svg style="position:absolute;left:0;top:0" width="643" height="219" viewBox="0 0 643 219"><path d="M0,206 C6,220 26,222 36,212 C44,208 60,215 110,216 C170,217 240,220 300,218 C360,216 380,204 420,206 C432,206 436,130 444,106 C450,93 460,90 472,92 C505,98 540,104 570,106 L634,106" fill="none" stroke="#6aab2e" stroke-width="0.8"/></svg>
  </section>

</div>
</body>
</html>
```